Company Profile
Korvane Cargo Sdn Bhd is a well-established and experienced freight forwarder in Kuala Lumpur, Malaysia. We specialize in air and sea forwarding, Custom Brokerage and regulatory compliance services, inland transportation, overseas freighting and warehousing and distribution management. With our dedicated qualified and experienced professionals, we are fully committed to serving our clients.

Our Mission
Based on the motto “Quick, Reliable and Polite”, Korvane Cargo is dedicated to upholding the following three points corporate philosophy:1. Adhering to the principle that “the customer always comes first”.2. Contributing to the development of the local community.3. Making it our duty to be responsible and sincere.

Our Edge
• One-Stop Logistics Solutions
• Extensive Network Throughout Malaysia
• Highly Qualified and Experienced Pool of Professionals
• Comprehensive IT Solutions
• Innovative and Customer-focused Solutions
• Flexible and Consistent in Managing Exceptions
• Total Supply Chain Visibility

Target Market : We sell the logistics services to all the industry in Malaysia. (One Stop Logistics Solutions)

Business Card Detail : I would like to see the logo on the front with the general info.

Must Haves :
1) Name, Title, Office, Cell, Fax, Email, Address, Website
2) Must have complete company name show as : Korvane Cargo Sdn Bhd
3) Must have company registration no, show as : 8571620-W

Nice to Haves : Modern Design Business Card

Target Market(s)

We sell the logistics services to all the industry in Malaysia. (One Stop Logistics Solutions)

Contact Information for Business Card

I would like to see the logo on the front with the general info.

Colors

Designer to choose colors to be used in the design.

Requirements
Must have
• 1) Name, Title, Office, Cell, Fax, Email, Address, Website
• 2) Must have complete company name show as : Korvane Cargo Sdn Bhd
• 3) Must have company registration no, show as : 8571620-W
Nice to have
• Modern Design Business Card
Should not have
• Nil

```html
<!DOCTYPE html>
<html lang="en">
<head>
<meta charset="utf-8">
<title>Korvane Cargo – Business Card</title>
<link href="https://fonts.googleapis.com/css2?family=Saira:wght@400;600&display=swap" rel="stylesheet">
<style>
  :root {
    --navy: #0b4d8a;
    --sky: #27a9e1;
    --ink: #232323;
    --paper: #ffffff;
    --backdrop: #eceeef;
  }
  * { margin: 0; padding: 0; box-sizing: border-box; }
  html, body { width: 1200px; height: 1028px; overflow: hidden; background: var(--backdrop); }
  body { position: relative; font-family: "Saira", sans-serif; color: var(--ink); }

  .card {
    position: absolute; left: 180px; width: 840px; height: 478px;
    border-radius: 28px; overflow: hidden;
  }
  .card-front { top: 18px; background: var(--paper); }
  .card-back { top: 532px; background: var(--navy); }

  .brand { position: absolute; display: flex; align-items: center; }
  .brand-mark { border-radius: 50%; flex: none; }
  .brand-name { font-weight: 600; line-height: 1; }
  .brand-name .line1 { display: block; }
  .brand-name .line2 { display: block; letter-spacing: 0.42em; }

  .card-front .brand { left: 41px; top: 41px; gap: 40px; }
  .card-front .brand-mark { width: 81px; height: 81px; border: 5px solid var(--navy); }
  .card-front .brand-name { color: var(--navy); }
  .card-front .brand-name .line1 { font-size: 42px; letter-spacing: 0.04em; }
  .card-front .brand-name .line2 { font-size: 24px; margin-top: 4px; }

  .person-name { position: absolute; left: 42px; top: 176px; font-size: 31px; font-weight: 600; color: var(--sky); letter-spacing: 0.01em; }
  .person-title { position: absolute; left: 42px; top: 220px; font-size: 20px; }

  .contacts { position: absolute; left: 42px; top: 272px; list-style: none; }
  .contacts li { display: flex; align-items: center; height: 27px; font-size: 19.5px; }
  .contacts svg { width: 16px; height: 16px; margin-right: 14px; flex: none; }

  .divider { position: absolute; left: 436px; top: 270px; width: 2px; height: 136px; background: var(--sky); }

  .office { position: absolute; left: 484px; top: 262px; }
  .office-company { font-size: 24px; font-weight: 600; color: var(--sky); }
  .office-address { font-size: 19.5px; line-height: 27px; margin-top: 4px; font-style: normal; }

  .footer-band { position: absolute; left: 0; bottom: 0; width: 100%; height: 35px; background: var(--navy); }
  .tagline { position: absolute; left: 43px; top: 3px; color: #fff; font-size: 19.5px; }
  .reg-no {
    position: absolute; left: 482px; top: -3px; width: 188px; height: 38px;
    background: var(--sky); border: 3px solid #fff; border-bottom: none;
    color: #fff; font-size: 19.5px; text-align: center; line-height: 34px;
  }

  .card-back .brand { left: 128px; top: 176px; gap: 56px; }
  .card-back .brand-mark { width: 128px; height: 128px; border: 6px solid #fff; }
  .card-back .brand-name { color: #fff; }
  .card-back .brand-name .line1 { font-size: 62px; letter-spacing: 0.04em; }
  .card-back .brand-name .line2 { font-size: 36px; margin-top: 6px; }
</style>
</head>
<body>

<section class="card card-front">
  <div class="brand">
    <span class="brand-mark"></span>
    <div class="brand-name"><span class="line1">KORVANE</span><span class="line2">CARGO</span></div>
  </div>

  <h1 class="person-name">DANIEL TEOH</h1>
  <p class="person-title">Managing Director</p>

  <ul class="contacts">
    <li>
      <svg viewBox="0 0 16 16"><rect x="4" y="1" width="8" height="14" rx="1.5" fill="none" stroke="var(--sky)" stroke-width="1.6"/><circle cx="8" cy="12.5" r="0.9" fill="var(--sky)"/></svg>
      (+6012) 586 2107
    </li>
    <li>
      <svg viewBox="0 0 16 16"><path d="M4 1.5 6.5 5 5 6.5c.8 1.8 2.2 3.3 4.5 4.5L11 9.5l3.5 2.5-1.5 2.5C7.5 14.5 1.5 8.5 1.5 3z" fill="none" stroke="var(--sky)" stroke-width="1.4" stroke-linejoin="round"/></svg>
      (+603) 3281 7650 / 7651
    </li>
    <li>
      <svg viewBox="0 0 16 16"><rect x="4" y="1.5" width="8" height="4" fill="var(--sky)"/><rect x="1" y="6" width="14" height="6" rx="1.5" fill="var(--sky)"/><rect x="4" y="10" width="8" height="4.5" fill="#fff" stroke="var(--sky)" stroke-width="1.2"/></svg>
      (+603) 3281 7652
    </li>
    <li>
      <svg viewBox="0 0 16 16"><rect x="1.5" y="3.5" width="13" height="9" fill="none" stroke="var(--sky)" stroke-width="1.4"/><path d="M1.5 3.5 8 9l6.5-5.5" fill="none" stroke="var(--sky)" stroke-width="1.4"/></svg>
      daniel.teoh@korvanecargo.com.my
    </li>
    <li>
      <svg viewBox="0 0 16 16"><circle cx="8" cy="8" r="6.5" fill="none" stroke="var(--sky)" stroke-width="1.3"/><ellipse cx="8" cy="8" rx="3" ry="6.5" fill="none" stroke="var(--sky)" stroke-width="1.1"/><path d="M1.5 8h13M2.5 4.8h11M2.5 11.2h11" stroke="var(--sky)" stroke-width="1.1"/></svg>
      www.korvanecargo.com.my
    </li>
  </ul>

  <div class="divider"></div>

  <div class="office">
    <h2 class="office-company">Korvane Cargo Sdn Bhd</h2>
    <address class="office-address">
      No.28B, 2nd Floor,<br>
      Jalan Seri Mutiara 3/KS9,<br>
      Taman Sentosa Indah, 41300 Klang,<br>
      Selangor Darul Ehsan, Malaysia.
    </address>
  </div>

  <div class="footer-band">
    <span class="tagline">One Stop Logistics Specialist</span>
    <span class="reg-no">8571620-W</span>
  </div>
</section>

<section class="card card-back">
  <div class="brand">
    <span class="brand-mark"></span>
    <div class="brand-name"><span class="line1">KORVANE</span><span class="line2">CARGO</span></div>
  </div>
</section>

</body>
</html>
```